New York IT Service, Technology & Security Co.

need a new business card design for our Technology & Security Company. We are a Computer Networking Company, Security Camera Installers, Phone Systems.

Target Market(s)

Construction, Medical, Law Offices, Accounting, Retail etc.

Industry/Entity Type

Information Technology

Logo is attached, colors are Blue, Red, Black. Blue for Technology & Red is for Security Cameras, Access Control, Alarm Systems

Colors
fbed22
ec1f27
0555a3
ffffff

Requirements
Must have
• Pictures or Icons for
• For Technology:
• Computer, Network, Phone System, Copier, TV, Cabling
• For Security:
• Video Surveillance, Access Control, Intercom, Fire Alarm, Burglar Alarm, Time Clock

```html
<!DOCTYPE html>
<html lang="en">
<head>
<meta charset="utf-8">
<title>Harbor Line IT Service – Business Card</title>
<link href="https://fonts.googleapis.com/css2?family=Source+Sans+3:wght@400;600;700;800&family=Roboto:wght@400;700&display=swap" rel="stylesheet">
<style>
  :root {
    --tech-blue: #0a6cb5;
    --brand-blue: #0555a3;
    --security-red: #ec1f27;
    --card-black: #1c1c1c;
    --white: #ffffff;
    --paper: #f4f4f4;
    --text-gray: #444444;
    --stage: #e6e3df;
  }
  * { margin: 0; padding: 0; box-sizing: border-box; }
  html, body {
    width: 1200px; height: 960px; overflow: hidden;
    background: var(--stage);
  }
  .canvas { position: relative; width: 1200px; height: 960px; }
  .card {
    position: absolute; width: 600px; height: 342px; overflow: hidden;
    box-shadow: 0 3px 8px rgba(0,0,0,.25);
  }
  /* Front */
  .card-front { left: 314px; top: 113px; background: var(--card-black); }
  .front-blue {
    position: absolute; left: 0; top: 0; width: 300px; height: 342px;
    background: var(--tech-blue);
  }
  .front-art {
    position: absolute; left: 130px; top: 0; width: 410px; height: 342px;
  }
  .front-brand {
    position: absolute; right: 26px; top: 58px;
    display: flex; align-items: center; gap: 8px;
    font-family: "Source Sans 3", sans-serif; font-weight: 800;
    font-size: 21px; color: var(--white); text-transform: uppercase; letter-spacing: .2px;
  }
  .brand-dot { width: 12px; height: 12px; border-radius: 50%; background: var(--security-red); }
  .contact {
    position: absolute; left: 28px; top: 166px;
    font-family: "Source Sans 3", sans-serif; color: var(--white);
  }
  .contact-name { font-size: 22px; font-weight: 700; line-height: 1.1; }
  .contact-role { font-size: 15px; margin-top: 4px; }
  .contact-address { font-size: 15px; line-height: 19px; margin-top: 9px; }
  .contact-list { list-style: none; margin-top: 8px; font-size: 15px; line-height: 19.5px; }
  .contact-list li { display: flex; align-items: center; gap: 8px; }
  .contact-list svg { width: 13px; height: 13px; fill: var(--white); flex: none; }
  /* Back */
  .card-back { left: 311px; top: 472px; background: var(--paper); text-align: center; }
  .back-brand {
    margin-top: 82px; display: inline-flex; align-items: center; gap: 10px;
    font-family: "Source Sans 3", sans-serif; font-weight: 800;
    font-size: 30px; color: var(--card-black); text-transform: uppercase;
  }
  .back-brand .brand-dot { width: 16px; height: 16px; }
  .service-group { font-family: "Roboto", sans-serif; }
  .service-group h2 {
    font-family: "Source Sans 3", sans-serif; font-weight: 700; font-size: 16px;
    letter-spacing: .2px;
  }
  .service-group p { font-size: 14px; color: var(--text-gray); line-height: 18px; }
  .service-tech { margin-top: 32px; }
  .service-tech h2 { color: var(--tech-blue); }
  .service-security { margin-top: 13px; }
  .service-security h2 { color: var(--security-red); }
  .sep { display: inline-block; width: 5px; height: 5px; border-radius: 50%; margin: 0 3px; vertical-align: middle; }
  .service-tech .sep { background: var(--tech-blue); }
  .service-security .sep { background: var(--security-red); }
</style>
</head>
<body>
<main class="canvas">
  <section class="card card-front">
    <div class="front-blue"></div>
    <svg class="front-art" viewBox="0 0 410 342" role="img" aria-label="Large decorative brand graphic area">
      <defs>
        <linearGradient id="artTone" x1="0" y1="0" x2="1" y2="1">
          <stop offset="0" stop-color="#ec1f27" stop-opacity=".55"/>
          <stop offset=".5" stop-color="#f08a74" stop-opacity=".35"/>
          <stop offset="1" stop-color="#2a6ec0" stop-opacity=".45"/>
        </linearGradient>
      </defs>
      <rect x="0" y="0" width="410" height="342" fill="url(#artTone)"/>
    </svg>
    <div class="front-brand"><span class="brand-dot"></span>Harbor Line IT Service</div>
    <div class="contact">
      <div class="contact-name">DANIEL REYES</div>
      <div class="contact-role">CEO/FOUNDER</div>
      <div class="contact-address">4120 Cedar Hollow Road<br>Fairbanks, Alaska 99701</div>
      <ul class="contact-list">
        <li><svg viewBox="0 0 16 16"><path d="M2 5c0-2 2-3 6-3s6 1 6 3v1h-3V5H5v1H2zM4 8h8l2 6H2z"/></svg>555 214 0193</li>
        <li><svg viewBox="0 0 16 16"><path d="M1 4h14v1L8 9 1 5zM1 6.5l7 4 7-4V12H1z"/></svg>daniel@HarborLineIT.com</li>
        <li><svg viewBox="0 0 16 16"><circle cx="8" cy="8" r="7"/></svg>www.HarborLineIT.com</li>
      </ul>
    </div>
  </section>

  <section class="card card-back">
    <div class="back-brand"><span class="brand-dot"></span>Harbor Line IT Service</div>
    <div class="service-group service-tech">
      <h2>FOR TECHNOLOGY</h2>
      <p>Computer<span class="sep"></span>Network<span class="sep"></span>Phone System</p>
      <p>Copier<span class="sep"></span>TV<span class="sep"></span>Cabling</p>
    </div>
    <div class="service-group service-security">
      <h2>FOR SECURITY</h2>
      <p>Video Surveillance<span class="sep"></span>Access Control<span class="sep"></span>Intercom</p>
      <p>Fire Alarm<span class="sep"></span>Burglar Alarm<span class="sep"></span>Time Clock</p>
    </div>
  </section>
</main>
</body>
</html>
```